Need Help Rebranding My Food Blog

I have a Wordpress Food blog called BeetBuddies.com. Right now it has no life and is very bland. I am rebranding this site to a new named called, TheHoneyedPath.com. I would love to have a blog that is vibrant and full of life and personality.

One of my top priorities when a new visitor comes to my site is to quickly understand what the site is about (Gluten-free, dairy-free sweets that taste delicious).

I also want people to feel a connection with me when they come to the site.

Here are some other things that I'd like in the blog design...

1. Optin
My business is driven by adding people to my list so it is very important for me to have an optin front and center/ above-the-fold. See https://www.clevertidyearnings.com/ as an example. The headline that I would like is "Gluten-free & dairy-free sweets that actually taste good"

2. Vibrant/full life
The next important aspect of this blog is that it is vibrant. I like colors that remind me of a SUNSET. See attachments for logo and color scheme. Here's an example of a site I really like that is vibrant: http://www.sugarandopendays.com/

Also see Image titled: "Sample: Feeling". Notice the feeling you get from the image/brush strokes and how it feels light, breezy, and free spirited.

3. Food Images
The last important aspect for my blog is to showcase my recipes. I have attached a few of them as examples. Its really important for a food blog to showcase beautiful pictures of recipes for people to see so will definitely need this in the design.

Also, attached...
1. Image of me.
2. New logo for TheHoneyedPath (notice: don't use the one attached as "Sample/Feeling". That's just for reference of the feeling I like.)

Thanks!

Marion

P.S. I didn't include all the copy that would be needed so feel free to use the "lorem ipsum" text as placeholder if need be.

Target Market(s)

stay-at-home moms, dairy-free & gluten allergies, love desserts & sweets

Coding

Coded - Design and coding required

Font styles to use
Sans Serif

Requirements
Must have
• 1. Optin area with my picture and what I'm about ""Gluten-free & dairy-free sweets that actually taste good""
• 2. Must have personality/vibrancy to the site. Think full of life, not dull like my current website... beetbuddies.com
• 3. Highlight food images (Vertical image holders only)
Nice to have
• Color scheme should be based on my logo
Should not have
• No black or grey colors

```html
<!DOCTYPE html>
<html lang="en">
<head>
<meta charset="utf-8">
<title>TheHoneyedPath — Gluten-free &amp; dairy-free sweets</title>
<link rel="stylesheet" href="https://fonts.googleapis.com/css2?family=Open+Sans:ital,wght@0,400;0,600;0,700;1,400&display=swap">
<style>
:root{
  --pink:#dc2657;
  --pink-deep:#c81e4e;
  --orange:#ef7a36;
  --orange-warm:#f2873a;
  --ink:#2b2b2b;
  --text:#555555;
  --muted:#8a8a8a;
  --paper:#ffffff;
  --page:#ececec;
  --line:#e4e4e4;
  --fb:#2c4f86;
  --tw:#3aa6dc;
  --rss:#f07a28;
}
*{box-sizing:border-box;margin:0;padding:0}
html,body{width:1200px;height:2432px;overflow:hidden}
body{font-family:"Open Sans",Arial,sans-serif;color:var(--text);background:var(--page);position:relative}
.abs{position:absolute}

/* header */
.site-header{left:0;top:0;width:1200px;height:101px;background:linear-gradient(180deg,var(--pink-deep) 0,var(--pink) 6%,var(--orange) 100%)}
.brand{left:86px;top:30px;font-size:26px;font-weight:600;color:#fff;letter-spacing:.2px}
.main-nav{left:363px;top:42px;font-size:15px;color:#fff}
.main-nav a{color:#fff;text-decoration:none;text-transform:uppercase;position:absolute;white-space:nowrap;transform:translateX(-50%)}
.main-nav .active{border:2px solid #fff;border-radius:16px;padding:3px 14px}
.search-btn{left:1070px;top:36px;width:33px;height:32px;border:2px solid #fff}

/* hero */
.hero{left:0;top:101px;width:1200px;height:505px;overflow:hidden;
  background:radial-gradient(ellipse 560px 330px at 420px 250px,rgba(160,110,60,.55),rgba(200,170,120,.25) 60%,transparent 80%),
  radial-gradient(ellipse 400px 140px at 430px 330px,rgba(150,190,90,.45),transparent 70%),
  linear-gradient(90deg,#f3ece2,#efe6da 60%,#e9e4e6)}
.hero-veil{inset:0;background:rgba(255,255,255,.35)}
.hero-title{left:88px;top:159px;color:var(--ink);text-transform:uppercase;line-height:1.3}
.hero-title .lead{display:block;font-size:27px;font-weight:600}
.hero-title .strong{display:block;font-size:33px;font-weight:600}
.optin-field{top:264px;width:228px;height:45px;background:#fff;border-radius:3px;box-shadow:0 2px 4px rgba(0,0,0,.18);font-size:13px;color:#555;padding:14px 17px;text-transform:uppercase}
.subscribe-btn{left:89px;top:334px;width:135px;height:38px;border-radius:19px;background:var(--pink);color:#fff;font-size:15px;text-align:center;line-height:38px;text-transform:uppercase}
.portrait{left:692px;top:41px;width:418px;height:418px;border-radius:50%;border:5px solid #fff;box-shadow:0 2px 8px rgba(0,0,0,.2);
  background:radial-gradient(circle at 55% 55%,#c9a590 0,#b5917c 30%,#d9d4c8 60%,#c7c3ba 100%)}

/* sections */
.section-title{font-size:22px;color:var(--ink);text-transform:uppercase;font-weight:400}
.dots{display:flex;gap:5px}
.dots i{width:8px;height:8px;border-radius:50%;background:#cfcfcf;display:block}
.dots i.on{background:#333}
.card{background:var(--paper);box-shadow:0 1px 4px rgba(0,0,0,.2)}

.blog-card{left:84px;width:693px;height:240px}
.blog-thumb{position:absolute;left:16px;top:28px;width:216px;height:186px;border:3px solid #fff;box-shadow:0 1px 4px rgba(0,0,0,.3)}
.blog-body{position:absolute;left:247px;top:26px;width:420px}
.blog-body h3{font-size:19px;font-weight:400;color:var(--ink)}
.blog-meta{font-size:11.5px;color:#555;margin-top:8px}
.blog-excerpt{font-size:13.5px;line-height:21px;color:#666;margin-top:11px}
.blog-actions{display:flex;align-items:center;gap:10px;margin-top:18px}
.learn-more{width:93px;height:27px;background:var(--orange);color:#fff;font-size:10.5px;font-weight:700;text-align:center;line-height:27px;text-transform:uppercase;margin-right:8px}
.share{width:19px;height:19px;border-radius:50%;display:block}

.stat{top:699px;width:97px;height:109px;color:#fff;text-align:center;font-size:13px;line-height:16px;padding-top:12px}
.stat .dot{width:46px;height:46px;border-radius:50%;background:rgba(0,0,0,.15);margin:0 auto 11px}

.panel-rule{border-top:3px solid var(--pink)}
.popular{left:798px;top:877px;width:313px;height:834px;padding:0 13px}
.pop-item{display:flex;gap:16px;height:106px;padding-top:24px;border-bottom:1px solid var(--line)}
.pop-thumb{width:82px;height:72px;flex:none}
.pop-text{font-size:13px;line-height:20px;color:var(--ink);width:172px}
.pop-icons{display:flex;gap:12px;margin-top:12px}
.pop-icons svg{width:13px;height:13px}
.view-more{position:absolute;left:0;right:0;top:784px;text-align:center;font-size:13px;font-style:italic;color:#444}

.most{left:86px;top:1795px;width:692px;height:312px}
.most-item{position:absolute;top:34px;width:198px}
.most-thumb{height:138px}
.most-item p{font-size:14px;line-height:21px;color:var(--ink);margin-top:12px}
.most-date{display:flex;align-items:center;gap:10px;font-size:13px;color:#555;margin-top:34px}
.categories{left:796px;top:1795px;width:312px;height:312px;padding:26px 0 0 26px}
.categories li{list-style:none;font-size:14px;color:#444;height:32px}

/* footer */
.site-footer{left:0;top:2166px;width:1200px;height:266px;background:linear-gradient(180deg,var(--pink) 0,var(--orange-warm) 100%);color:#fff}
.footer-brand{left:86px;top:100px;font-size:24px;font-weight:600}
.footer-col{top:42px}
.footer-col h4{font-size:15px;font-weight:400;text-transform:uppercase;margin-bottom:16px}
.footer-col p{font-size:11.5px;line-height:23px}
.mail-row{display:flex;margin-top:14px}
.mail-row .field{width:148px;height:31px;background:#fff;color:#555;font-size:11.5px;padding:8px 9px}
.mail-row .btn{width:55px;height:31px;background:#222;color:#fff;font-size:12px;line-height:31px;text-align:center}
.follow{display:flex;gap:17px;margin-top:26px}
.follow i{display:block;width:24px;height:24px;border-radius:4px;background:#fff}
.copyright{left:0;width:1200px;top:229px;text-align:center;font-size:12px}
</style>
</head>
<body>

<header class="site-header abs">
  <div class="brand abs">TheHoneyedPath</div>
  <nav class="main-nav abs">
    <a class="active" style="left:39px;top:-7px">Home</a>
    <a style="left:141px">About</a>
    <a style="left:253px">Recipes</a>
    <a style="left:380px">Resources</a>
    <a style="left:500px">Blog</a>
    <a style="left:615px">Contacts</a>
  </nav>
  <div class="search-btn abs">
    <svg width="29" height="28" viewBox="0 0 29 28"><circle cx="13.5" cy="13" r="4.5" fill="none" stroke="#fff" stroke-width="2"/><line x1="16.8" y1="16.3" x2="20" y2="19.5" stroke="#fff" stroke-width="2"/></svg>
  </div>
</header>

<section class="hero abs">
  <div class="hero-veil abs" role="img" aria-label="Softly blurred photo of a burger as background"></div>
  <h1 class="hero-title abs"><span class="lead">Gluten-free &amp; dairy-free sweets</span><span class="strong">that actually taste good</span></h1>
  <div class="optin-field abs" style="left:88px">Name</div>
  <div class="optin-field abs" style="left:330px">Email ID</div>
  <div class="subscribe-btn abs">Subscribe</div>
  <div class="portrait abs" role="img" aria-label="Circular portrait photo"></div>
</section>

<h2 class="section-title abs" style="left:88px;top:652px">Latest Blogs</h2>
<div class="dots abs" style="left:735px;top:662px"><i></i><i class="on"></i><i></i></div>

<article class="blog-card card abs" style="top:699px">
  <div class="blog-thumb" role="img" aria-label="Photo of chocolate bark with pretzels" style="background:linear-gradient(135deg,#5a3a2a,#c88a50 50%,#3e2a20)"></div>
  <div class="blog-body">
    <h3>Neque porro quisquam est qui dolorem ipsum</h3>
    <div class="blog-meta">Author : admin &nbsp;|&nbsp; Post id : 12365 &nbsp;|&nbsp; Post on : October 1, 2017 &nbsp;|&nbsp; 5 Comments</div>
    <p class="blog-excerpt">Sed id tincidunt arcu. Maecenas eget elit at purus dapibus dictum. Vestibulum ante ipsum primis in faucibus orci luctus et ultrices posuere cubilia Curae; In hac habitasse platea dictumst.</p>
    <div class="blog-actions"><span class="learn-more">Learn More</span><i class="share" style="background:#3aa6dc"></i><i class="share" style="background:#2c4f86"></i><i class="share" style="background:#c9302c"></i><i class="share" style="background:#e0245e"></i><i class="share" style="background:#c4302b"></i></div>
  </div>
</article>

<article class="blog-card card abs" style="top:955px">
  <div class="blog-thumb" role="img" aria-label="Photo of a pink frosted heart cookie" style="background:linear-gradient(135deg,#8a9a8a,#e8605a 35%,#f07a78 70%,#7d8d80)"></div>
  <div class="blog-body">
    <h3>Neque porro quisquam est qui dolorem ipsum</h3>
    <div class="blog-meta">Author : admin &nbsp;|&nbsp; Post id : 12365 &nbsp;|&nbsp; Post on : October 1, 2017 &nbsp;|&nbsp; 5 Comments</div>
    <p class="blog-excerpt">Sed id tincidunt arcu. Maecenas eget elit at purus dapibus dictum. Vestibulum ante ipsum primis in faucibus orci luctus et ultrices posuere cubilia Curae; In hac habitasse platea dictumst.</p>
    <div class="blog-actions"><span class="learn-more">Learn More</span><i class="share" style="background:#3aa6dc"></i><i class="share" style="background:#2c4f86"></i><i class="share" style="background:#c9302c"></i><i class="share" style="background:#e0245e"></i><i class="share" style="background:#c4302b"></i></div>
  </div>
</article>

<article class="blog-card card abs" style="top:1213px">
  <div class="blog-thumb" role="img" aria-label="Photo of a bowl of creamy soup" style="background:radial-gradient(circle at 45% 55%,#f0dcae 0,#e8cf9a 45%,#ffffff 60%,#d8c08a 100%)"></div>
  <div class="blog-body">
    <h3>Neque porro quisquam est qui dolorem ipsum</h3>
    <div class="blog-meta">Author : admin &nbsp;|&nbsp; Post id : 12365 &nbsp;|&nbsp; Post on : October 1, 2017 &nbsp;|&nbsp; 5 Comments</div>
    <p class="blog-excerpt">Sed id tincidunt arcu. Maecenas eget elit at purus dapibus dictum. Vestibulum ante ipsum primis in faucibus orci luctus et ultrices posuere cubilia Curae; In hac habitasse platea dictumst.</p>
    <div class="blog-actions"><span class="learn-more">Learn More</span><i class="share" style="background:#3aa6dc"></i><i class="share" style="background:#2c4f86"></i><i class="share" style="background:#c9302c"></i><i class="share" style="background:#e0245e"></i><i class="share" style="background:#c4302b"></i></div>
  </div>
</article>

<article class="blog-card card abs" style="top:1471px">
  <div class="blog-thumb" role="img" aria-label="Photo of caramel popcorn" style="background:linear-gradient(135deg,#d8703a,#f3d2b0 40%,#e0884a 70%,#c85a30)"></div>
  <div class="blog-body">
    <h3>Neque porro quisquam est qui dolorem ipsum</h3>
    <div class="blog-meta">Author : admin &nbsp;|&nbsp; Post id : 12365 &nbsp;|&nbsp; Post on : October 1, 2017 &nbsp;|&nbsp; 5 Comments</div>
    <p class="blog-excerpt">Sed id tincidunt arcu. Maecenas eget elit at purus dapibus dictum. Vestibulum ante ipsum primis in faucibus orci luctus et ultrices posuere cubilia Curae; In hac habitasse platea dictumst.</p>
    <div class="blog-actions"><span class="learn-more">Learn More</span><i class="share" style="background:#3aa6dc"></i><i class="share" style="background:#2c4f86"></i><i class="share" style="background:#c9302c"></i><i class="share" style="background:#e0245e"></i><i class="share" style="background:#c4302b"></i></div>
  </div>
</article>

<div class="stat abs" style="left:798px;background:var(--fb)"><div class="dot"></div>259<br>fans</div>
<div class="stat abs" style="left:905px;background:var(--tw)"><div class="dot"></div>568<br>followers</div>
<div class="stat abs" style="left:1013px;background:var(--rss)"><div class="dot"></div>101<br>subscribers</div>

<h2 class="section-title abs" style="left:797px;top:845px;font-size:21px">Popular Posts</h2>
<aside class="popular card panel-rule abs">
  <div class="pop-item"><div class="pop-thumb" role="img" aria-label="Photo of a sandwich" style="background:linear-gradient(180deg,#d8a060,#7a9a50 50%,#c08050)"></div><div><p class="pop-text">Ipsum is simply dummy text of the printing and type</p><div class="pop-icons"><svg viewBox="0 0 13 13"><path d="M6.5 1l1.6 3.4 3.7.4-2.8 2.5.8 3.7-3.3-1.9-3.3 1.9.8-3.7L1.2 4.8l3.7-.4z" fill="none" stroke="#777"/></svg><svg viewBox="0 0 13 13"><rect x="1.5" y="2.5" width="10" height="9" fill="none" stroke="#777"/><line x1="1.5" y1="5" x2="11.5" y2="5" stroke="#777"/></svg><svg viewBox="0 0 13 13"><circle cx="6.5" cy="4.5" r="2.5" fill="none" stroke="#777"/><path d="M2 12c0-3 2-4.5 4.5-4.5S11 9 11 12" fill="none" stroke="#777"/></svg></div></div></div>
  <div class="pop-item"><div class="pop-thumb" role="img" aria-label="Photo of a brownie" style="background:linear-gradient(135deg,#8a4a2a,#b0673a 60%,#e8e2d8)"></div><div><p class="pop-text">Ipsum is simply dummy text of the printing and type</p><div class="pop-icons"><svg viewBox="0 0 13 13"><rect x="1.5" y="2.5" width="10" height="9" fill="none" stroke="#777"/><line x1="1.5" y1="5" x2="11.5" y2="5" stroke="#777"/></svg><svg viewBox="0 0 13 13"><circle cx="6.5" cy="4.5" r="2.5" fill="none" stroke="#777"/><path d="M2 12c0-3 2-4.5 4.5-4.5S11 9 11 12" fill="none" stroke="#777"/></svg><svg viewBox="0 0 13 13"><path d="M1.5 2.5h10v7H6l-3 2.5V9.5H1.5z" fill="none" stroke="#777"/></svg></div></div></div>
  <div class="pop-item"><div class="pop-thumb" role="img" aria-label="Photo of a dessert cup" style="background:linear-gradient(135deg,#c86a20,#f0a040 50%,#e8d8c0)"></div><div><p class="pop-text">Ipsum is simply dummy text of the printing and type</p><div class="pop-icons"><svg viewBox="0 0 13 13"><path d="M6.5 1l1.6 3.4 3.7.4-2.8 2.5.8 3.7-3.3-1.9-3.3 1.9.8-3.7L1.2 4.8l3.7-.4z" fill="none" stroke="#777"/></svg><svg viewBox="0 0 13 13"><rect x="1.5" y="2.5" width="10" height="9" fill="none" stroke="#777"/><line x1="1.5" y1="5" x2="11.5" y2="5" stroke="#777"/></svg><svg viewBox="0 0 13 13"><circle cx="6.5" cy="4.5" r="2.5" fill="none" stroke="#777"/><path d="M2 12c0-3 2-4.5 4.5-4.5S11 9 11 12" fill="none" stroke="#777"/></svg><svg viewBox="0 0 13 13"><path d="M1.5 2.5h10v7H6l-3 2.5V9.5H1.5z" fill="none" stroke="#777"/></svg></div></div></div>
  <div class="pop-item"><div class="pop-thumb" role="img" aria-label="Photo of a bowl of soup" style="background:radial-gradient(circle,#e8a050 0,#d88a3a 55%,#9a8870)"></div><div><p class="pop-text">Ipsum is simply dummy text of the printing and type</p><div class="pop-icons"><svg viewBox="0 0 13 13"><rect x="1.5" y="2.5" width="10" height="9" fill="none" stroke="#777"/><line x1="1.5" y1="5" x2="11.5" y2="5" stroke="#777"/></svg><svg viewBox="0 0 13 13"><circle cx="6.5" cy="4.5" r="2.5" fill="none" stroke="#777"/><path d="M2 12c0-3 2-4.5 4.5-4.5S11 9 11 12" fill="none" stroke="#777"/></svg><svg viewBox="0 0 13 13"><path d="M1.5 2.5h10v7H6l-3 2.5V9.5H1.5z" fill="none" stroke="#777"/></svg></div></div></div>
  <div class="pop-item"><div class="pop-thumb" role="img" aria-label="Photo of a cookie ball" style="background:radial-gradient(circle,#a05a38 0,#8a4a2e 50%,#e0dcd6 75%)"></div><div><p class="pop-text">Ipsum is simply dummy text of the printing and type</p><div class="pop-icons"><svg viewBox="0 0 13 13"><rect x="1.5" y="2.5" width="10" height="9" fill="none" stroke="#777"/><line x1="1.5" y1="5" x2="11.5" y2="5" stroke="#777"/></svg><svg viewBox="0 0 13 13"><circle cx="6.5" cy="4.5" r="2.5" fill="none" stroke="#777"/><path d="M2 12c0-3 2-4.5 4.5-4.5S11 9 11 12" fill="none" stroke="#777"/></svg><svg viewBox="0 0 13 13"><path d="M1.5 2.5h10v7H6l-3 2.5V9.5H1.5z" fill="none" stroke="#777"/></svg></div></div></div>
  <div class="pop-item"><div class="pop-thumb" role="img" aria-label="Photo of pistachio bites" style="background:linear-gradient(135deg,#6a5a30,#a0a050 50%,#5a4a28)"></div><div><p class="pop-text">Ipsum is simply dummy text of the printing and type</p><div class="pop-icons"><svg viewBox="0 0 13 13"><rect x="1.5" y="2.5" width="10" height="9" fill="none" stroke="#777"/><line x1="1.5" y1="5" x2="11.5" y2="5" stroke="#777"/></svg><svg viewBox="0 0 13 13"><circle cx="6.5" cy="4.5" r="2.5" fill="none" stroke="#777"/><path d="M2 12c0-3 2-4.5 4.5-4.5S11 9 11 12" fill="none" stroke="#777"/></svg><svg viewBox="0 0 13 13"><path d="M1.5 2.5h10v7H6l-3 2.5V9.5H1.5z" fill="none" stroke="#777"/></svg></div></div></div>
  <div class="pop-item"><div class="pop-thumb" role="img" aria-label="Photo of chocolate bark" style="background:linear-gradient(135deg,#5a3a2a,#c88a50 50%,#3e2a20)"></div><div><p class="pop-text">Ipsum is simply dummy text of the printing and type</p><div class="pop-icons"><svg viewBox="0 0 13 13"><rect x="1.5" y="2.5" width="10" height="9" fill="none" stroke="#777"/><line x1="1.5" y1="5" x2="11.5" y2="5" stroke="#777"/></svg><svg viewBox="0 0 13 13"><circle cx="6.5" cy="4.5" r="2.5" fill="none" stroke="#777"/><path d="M2 12c0-3 2-4.5 4.5-4.5S11 9 11 12" fill="none" stroke="#777"/></svg><svg viewBox="0 0 13 13"><path d="M1.5 2.5h10v7H6l-3 2.5V9.5H1.5z" fill="none" stroke="#777"/></svg></div></div></div>
  <div class="view-more">VIEW MORE</div>
</aside>

<h2 class="section-title abs" style="left:86px;top:1758px">Most Posts</h2>
<div class="dots abs" style="left:732px;top:1768px"><i></i><i class="on"></i><i></i></div>
<section class="most card panel-rule abs">
  <div class="most-item" style="left:24px"><div class="most-thumb" role="img" aria-label="Photo of chocolate glazed doughnuts" style="background:radial-gradient(circle at 50% 40%,#6a3a28 0,#4a2618 45%,#ece8e4 75%)"></div><p>Ipsum is simply dummy text of the printing and type</p><div class="most-date"><svg width="14" height="13" viewBox="0 0 14 13"><rect x="1" y="1.5" width="12" height="10.5" fill="none" stroke="#888"/><line x1="1" y1="4.5" x2="13" y2="4.5" stroke="#888"/></svg>27 March, 2017</div></div>
  <div class="most-item" style="left:245px"><div class="most-thumb" role="img" aria-label="Photo of pumpkin pudding in a bowl" style="background:linear-gradient(160deg,#d87a30,#e0a050 45%,#f2ece0 70%,#c8b8a0)"></div><p>Ipsum is simply dummy text of the printing and type</p><div class="most-date"><svg width="14" height="13" viewBox="0 0 14 13"><rect x="1" y="1.5" width="12" height="10.5" fill="none" stroke="#888"/><line x1="1" y1="4.5" x2="13" y2="4.5" stroke="#888"/></svg>7 March, 2017</div></div>
  <div class="most-item" style="left:465px"><div class="most-thumb" role="img" aria-label="Photo of watermelon ice pops" style="background:linear-gradient(135deg,#e8463a,#f07060 50%,#b8c0b8)"></div><p>Ipsum is simply dummy text of the printing and type</p><div class="most-date"><svg width="14" height="13" viewBox="0 0 14 13"><rect x="1" y="1.5" width="12" height="10.5" fill="none" stroke="#888"/><line x1="1" y1="4.5" x2="13" y2="4.5" stroke="#888"/></svg>1 January, 2017</div></div>
</section>

<h2 class="section-title abs" style="left:797px;top:1758px;font-size:21px">Categories</h2>
<ul class="categories card panel-rule abs">
  <li>Breakfast (12)</li><li>Dessert (22)</li><li>Dinner (16)</li><li>Lunch (11)</li><li>Resources (14)</li><li>Snack (19)</li><li>Uncategorized (1)</li><li>Vegan (28)</li>
</ul>

<footer class="site-footer abs">
  <div class="footer-brand abs">TheHoneyedPath</div>
  <div class="footer-col abs" style="left:313px">
    <h4>Contact Us</h4>
    <p>Address : 12 Orchard Lane, Harbour Row<br>Exeter, EX4 7QL<br>Phone : +44 1392 555 018<br>Email : hello@thehoneyedpath.com</p>
  </div>
  <div class="footer-col abs" style="left:632px">
    <h4>Join Our Mailing List</h4>
    <p style="line-height:18px;width:210px">Your about us information would fit here nicely.</p>
    <div class="mail-row"><span class="field">Email address</span><span class="btn">Submit</span></div>
  </div>
  <div class="footer-col abs" style="left:937px">
    <h4>Follow Us Out There</h4>
    <div class="follow"><i></i><i></i><i></i><i></i></div>
  </div>
  <p class="copyright abs">Copyright © 2017. All Rights Reserved</p>
</footer>

</body>
</html>
```